Vintage label design for Electrical company (stickers)

I'm after a vintage label design for my electrical company, currently trying to break into the upper market in the electrical field so I need something that stands out and is easy to read.
These will be getting made into stickers roughly 90-110mm x 40-60mm with a custom rectangular shape.
The stickers should have

Target Market(s)

Upper electrical market

Industry/Entity Type

Electrical

Font styles to use
Serif
Decorative
Script

Colors
acd037
9ccb3b
33b8a4

Requirements
Must have
• Be unique, edgy, vintage/retro and easy to read. An electrical theme
• Company logo (picture provided below obviously a lime)
• Cobalt Wiring
• 0492815037
• Cobaltwiring.com
• Facebook symbol
• as these are going to be stickers I would like my contact details on them
Nice to have
• Same shades of green, fit between 90-110mm x 40-60mm

```html
<!DOCTYPE html>
<html lang="en">
<head>
<meta charset="utf-8">
<title>Cobalt Wiring — Sticker Label</title>
<link rel="stylesheet" href="https://fonts.googleapis.com/css2?family=Kaushan+Script&family=Montserrat:wght@600&display=swap">
<style>
  :root {
    --label-green: #8cc63f;
    --deep-green: #0b5a1e;
    --bolt-yellow: #ffeb00;
    --paper: #ffffff;
  }
  html, body {
    margin: 0;
    padding: 0;
    width: 1200px;
    height: 670px;
    overflow: hidden;
    background: var(--paper);
  }
  .sticker {
    display: block;
    width: 1200px;
    height: 670px;
  }
  .label-body, .center-badge { fill: var(--label-green); }
  .frame-line {
    fill: none;
    stroke: var(--paper);
    stroke-width: 3;
    stroke-linecap: round;
  }
  .bolt { fill: var(--bolt-yellow); }
  .brand-mark { fill: var(--deep-green); }
  .contact {
    font-family: "Kaushan Script", cursive;
    fill: var(--deep-green);
  }
  .phone { font-size: 38px; }
  .website { font-size: 30px; }
  .established {
    font-family: "Montserrat", sans-serif;
    font-weight: 600;
    font-size: 13px;
    letter-spacing: 1.5px;
    fill: var(--paper);
  }
  .brand-name {
    font-family: "Kaushan Script", cursive;
    fill: var(--deep-green);
  }
  .brand-name--top { font-size: 100px; }
  .brand-name--bottom { font-size: 66px; }
</style>
</head>
<body>
<svg class="sticker" viewBox="0 0 1000 558" xmlns="http://www.w3.org/2000/svg">
  <!-- label body -->
  <rect class="label-body" x="130" y="80" width="738" height="390" rx="28"/>

  <!-- raised top tab of the centre badge -->
  <path class="center-badge" d="M412,90 L414,76 Q418,62 436,58 L515,26 Q525,22 534,29 L600,74 L600,90 Z"/>
  <!-- lower skirt of the centre badge -->
  <path class="center-badge" d="M340,430 L340,500 Q342,520 362,522 L668,532 Q690,533 690,512 L690,430 Z"/>

  <!-- frame lines -->
  <path class="frame-line" d="M410,101 L167,101 Q155,101 155,113 L155,425 Q155,437 167,437 L338,437"/>
  <path class="frame-line" d="M598,101 L833,101 Q845,101 845,113 L845,425 Q845,437 833,437 L692,437"/>

  <!-- lightning bolts -->
  <polygon class="bolt" points="212,146 262,146 236,182 258,182 186,236 214,192 192,192"/>
  <polygon class="bolt" points="786,146 736,146 762,182 740,182 812,236 784,192 806,192"/>

  <!-- brand -->
  <circle class="brand-mark" cx="505" cy="168" r="60"/>
  <text class="established" x="560" y="264" text-anchor="middle">EST. 2015</text>
  <text class="brand-name brand-name--top" x="510" y="360" text-anchor="middle">Cobalt</text>
  <text class="brand-name brand-name--bottom" x="515" y="445" text-anchor="middle">Wiring</text>

  <!-- contact details -->
  <text class="contact phone" x="0" y="0" text-anchor="middle" transform="translate(280,268) rotate(-56)">0492815037</text>
  <text class="contact website" x="0" y="0" text-anchor="middle" transform="translate(735,262) rotate(58)">Cobaltwiring.com</text>
</svg>
</body>
</html>
```